Consulting firm needs an infographic

The consulting we do needs a very graphic and understandable way to have perspective clients get exactly where we can help their company grow. I designed something that needs a lot of spice for it to look professional and relatable to them. This is being created to be used on a business card, as well as on posters, and social media.

```html
<!DOCTYPE html>
<html lang="en">
<head>
<meta charset="utf-8">
<title>Consulting Infographic</title>
<link rel="stylesheet" href="https://fonts.googleapis.com/css2?family=Poppins:wght@400;600;700;800&display=swap">
<style>
  :root{
    --dark:#333333;
    --white:#ffffff;
    --green:#3ab54a;
    --orange:#f15a2b;
    --blue-light:#1ea6e0;
    --blue-dark:#0b6db5;
    --road:#c8c8c8;
    --ink:#2b2b2b;
    --brand:#4a4a4a;
  }
  html,body{margin:0;padding:0;overflow:hidden;}
  body{width:1200px;height:848px;font-family:"Poppins",sans-serif;}
  .artboard{position:relative;width:1200px;height:848px;background:var(--white);overflow:hidden;}
  .panel-dark{position:absolute;left:0;top:0;width:600px;height:848px;background:var(--dark);}
  .infographic{position:absolute;left:0;top:0;width:1200px;height:848px;}
  .brand{position:absolute;left:975px;top:102px;display:flex;align-items:center;gap:7px;white-space:nowrap;}
  .brand-mark{width:10px;height:10px;background:var(--brand);}
  .brand-name{font-weight:600;font-size:14px;line-height:14px;color:var(--brand);}
  .num{font-family:"Poppins",sans-serif;font-weight:700;fill:var(--white);text-anchor:middle;}
  .label{font-family:"Poppins",sans-serif;font-weight:400;fill:var(--white);text-anchor:middle;}
  .hub-title{font-family:"Poppins",sans-serif;font-weight:800;fill:var(--ink);text-anchor:middle;}
  .hub-sub{font-family:"Poppins",sans-serif;font-weight:700;fill:var(--ink);text-anchor:middle;}
  .road{fill:none;stroke:var(--road);stroke-width:16;}
  .road-line{fill:none;stroke:var(--white);stroke-width:1.6;stroke-dasharray:7 6;}
  .chevron{fill:none;stroke:var(--white);stroke-width:4;stroke-linejoin:miter;stroke-linecap:butt;}
</style>
</head>
<body>
<main class="artboard">
  <div class="panel-dark"></div>

  <svg class="infographic" viewBox="0 0 1200 848" xmlns="http://www.w3.org/2000/svg">
    <defs>
      <filter id="soft-shadow" x="-30%" y="-30%" width="160%" height="160%">
        <feDropShadow dx="0" dy="3" stdDeviation="4" flood-color="#000" flood-opacity="0.3"/>
      </filter>
      <linearGradient id="blue-fill" x1="1" y1="0" x2="0" y2="1">
        <stop offset="0" stop-color="#1ea6e0"/>
        <stop offset="1" stop-color="#0b6db5"/>
      </linearGradient>
      <linearGradient id="hub-ring" x1="0" y1="0" x2="0" y2="1">
        <stop offset="0" stop-color="#f4f4f4"/>
        <stop offset="1" stop-color="#bdbdbd"/>
      </linearGradient>
      <g id="chev">
        <path class="chevron" d="M-8 0 L0 -8 L8 0"/>
        <path class="chevron" d="M-8 10 L0 2 L8 10"/>
      </g>
    </defs>

    <g class="diagram diagram-vertical">
      <path class="road" d="M215 220 A205 205 0 0 1 215 630"/>
      <path class="road-line" d="M215 220 A205 205 0 0 1 215 630"/>

      <path class="segment segment-green" fill="var(--green)" d="M215 425 L215 240 A185 185 0 0 1 371.9 327 Z"/>
      <path class="segment segment-orange" fill="var(--orange)" d="M215 425 L381.3 343.9 A185 185 0 0 1 381.3 506.1 Z"/>
      <path class="segment segment-blue" fill="url(#blue-fill)" d="M215 425 L371.9 523 A185 185 0 0 1 215 610 Z"/>

      <use href="#chev" transform="translate(262 334) rotate(20)"/>
      <use href="#chev" transform="translate(264 518) rotate(-20)"/>
      <use href="#chev" transform="translate(393 324) rotate(150)"/>
      <use href="#chev" transform="translate(396 527) rotate(208)"/>

      <g class="step step-01" filter="url(#soft-shadow)">
        <circle cx="303" cy="265" r="55" fill="var(--white)"/>
        <circle cx="303" cy="265" r="46" fill="var(--green)"/>
      </g>
      <text class="num" x="303" y="256" font-size="24">01</text>
      <line x1="278" y1="263" x2="328" y2="263" stroke="#2c8f39" stroke-width="1"/>
      <text class="label" x="303" y="277" font-size="7.5">Vendors</text>
      <text class="label" x="303" y="286" font-size="7.5">Resources</text>
      <text class="label" x="303" y="295" font-size="7.5">Costs</text>

      <g class="step step-02" filter="url(#soft-shadow)">
        <circle cx="390" cy="425" r="55" fill="var(--white)"/>
        <circle cx="390" cy="425" r="46" fill="var(--orange)"/>
      </g>
      <text class="num" x="390" y="410" font-size="24">02</text>
      <line x1="365" y1="418" x2="415" y2="418" stroke="#c84418" stroke-width="1"/>
      <text class="label" x="390" y="429" font-size="7.5">Executives</text>
      <text class="label" x="390" y="438" font-size="7.5">Administratives</text>
      <text class="label" x="390" y="447" font-size="7.5">Personnels</text>
      <text class="label" x="390" y="456" font-size="7.5">Logistics</text>

      <g class="step step-03" filter="url(#soft-shadow)">
        <circle cx="303" cy="590" r="55" fill="var(--white)"/>
        <circle cx="303" cy="590" r="46" fill="url(#blue-fill)"/>
      </g>
      <text class="num" x="303" y="576" font-size="24">03</text>
      <line x1="278" y1="584" x2="328" y2="584" stroke="#0a5c99" stroke-width="1"/>
      <text class="label" x="303" y="598" font-size="7.5">Customers</text>
      <text class="label" x="303" y="607" font-size="7.5">Identify &amp; B&amp;M</text>
      <text class="label" x="303" y="616" font-size="7.5">Revenue</text>

      <g class="hub" filter="url(#soft-shadow)">
        <circle cx="212" cy="430" r="78" fill="url(#hub-ring)"/>
        <circle cx="212" cy="430" r="68" fill="var(--white)"/>
      </g>
      <text class="hub-title" x="214" y="400" font-size="17">YOUR</text>
      <text class="hub-title" x="214" y="419" font-size="17">COMPANY</text>
      <text class="hub-sub" x="214" y="433" font-size="6.5">PRODUCTS/SERVICES</text>
      <line x1="172" y1="446" x2="256" y2="446" stroke="var(--ink)" stroke-width="1.4"/>
      <text class="hub-sub" x="214" y="463" font-size="7">Workforce |  Workplace</text>
      <text class="hub-sub" x="214" y="472" font-size="7">Workflow</text>
    </g>

    <g class="diagram diagram-horizontal">
      <path class="road" d="M685 492 A205 205 0 0 1 1095 492"/>
      <path class="road-line" d="M685 492 A205 205 0 0 1 1095 492"/>

      <path class="segment segment-green" fill="var(--green)" d="M890 492 L705 492 A185 185 0 0 1 783.9 340.5 Z"/>
      <path class="segment segment-orange" fill="var(--orange)" d="M890 492 L800.3 330.2 A185 185 0 0 1 979.7 330.2 Z"/>
      <path class="segment segment-blue" fill="url(#blue-fill)" d="M890 492 L996.1 340.5 A185 185 0 0 1 1075 492 Z"/>

      <use href="#chev" transform="translate(800 446) rotate(-90)"/>
      <use href="#chev" transform="translate(986 440) rotate(-90)"/>
      <use href="#chev" transform="translate(786 321) rotate(62)"/>
      <use href="#chev" transform="translate(992 319) rotate(118)"/>

      <g class="step step-01" filter="url(#soft-shadow)">
        <circle cx="715" cy="405" r="50" fill="var(--white)"/>
        <circle cx="715" cy="405" r="42" fill="var(--green)"/>
      </g>
      <text class="num" x="715" y="389" font-size="22">01</text>
      <line x1="692" y1="397" x2="738" y2="397" stroke="#2c8f39" stroke-width="1"/>
      <text class="label" x="715" y="411" font-size="7">Vendors</text>
      <text class="label" x="715" y="420" font-size="7">Resources</text>
      <text class="label" x="715" y="429" font-size="7">Costs</text>

      <g class="step step-02" filter="url(#soft-shadow)">
        <circle cx="888" cy="298" r="50" fill="var(--white)"/>
        <circle cx="888" cy="298" r="42" fill="var(--orange)"/>
      </g>
      <text class="num" x="888" y="284" font-size="22">02</text>
      <line x1="865" y1="292" x2="911" y2="292" stroke="#c84418" stroke-width="1"/>
      <text class="label" x="888" y="304" font-size="7">Executives</text>
      <text class="label" x="888" y="313" font-size="7">Administratives</text>
      <text class="label" x="888" y="322" font-size="7">Personnels</text>
      <text class="label" x="888" y="331" font-size="7">Logistics</text>

      <g class="step step-03" filter="url(#soft-shadow)">
        <circle cx="1063" cy="393" r="50" fill="var(--white)"/>
        <circle cx="1063" cy="393" r="42" fill="url(#blue-fill)"/>
      </g>
      <text class="num" x="1063" y="390" font-size="22">03</text>
      <line x1="1040" y1="398" x2="1086" y2="398" stroke="#0a5c99" stroke-width="1"/>
      <text class="label" x="1063" y="412" font-size="7">Customers</text>
      <text class="label" x="1063" y="421" font-size="7">Identify &amp; B&amp;M</text>
      <text class="label" x="1063" y="430" font-size="7">Revenue</text>

      <g class="hub" filter="url(#soft-shadow)">
        <circle cx="893" cy="495" r="78" fill="url(#hub-ring)"/>
        <circle cx="893" cy="495" r="68" fill="var(--white)"/>
      </g>
      <text class="hub-title" x="895" y="466" font-size="17">YOUR</text>
      <text class="hub-title" x="895" y="485" font-size="17">COMPANY</text>
      <text class="hub-sub" x="895" y="499" font-size="6.5">PRODUCTS/SERVICES</text>
      <line x1="853" y1="512" x2="937" y2="512" stroke="var(--ink)" stroke-width="1.4"/>
      <text class="hub-sub" x="895" y="529" font-size="7">Workforce |  Workplace</text>
      <text class="hub-sub" x="895" y="538" font-size="7">Workflow</text>
    </g>
  </svg>

  <div class="brand">
    <span class="brand-mark"></span>
    <span class="brand-name">Meridian Counsel</span>
  </div>
</main>
</body>
</html>
```